****FLYER design - LAW FIRM ADVERTISEMENT****

We are a small law firm based in Los Angeles, CA. We need an flyer used for advertising that we will be passing out. We want the flyer to be about 4in x 6in.

We want the flyer to advertise the name of our firm: MORVANTE KELDRIC LLP (no period)
- We want our group photo to take up a good portion of the flyer (although it's okay if parts of the photo have wording over it.)

COLORS: Our firm colors are different shades of steal/metal grey with a bit of a bold orange accent. Any bold writing, like our slogan, names of practice areas,... should be in orange.

We envision a horizontal lay-out of the flyer, but are open to creative options laid out vertically!

Feel free to play with the fonts, the sizing, the color combinations,...

We want the flyer to advertise our two areas of practice: PERSONAL INJURY and EMPLOYMENT LAW. Please also place each photo icon of our areas of practice somewhere around the name (ambulance photo for personal injury; person behind computer desk for employment law). The icons can be relatively small.

Under Personal Injury, please write:
If you or a loved one are suffering from an injury or wrongful death caused by the careless or intentional acts of others, then you have the right to pursue compensation for your injury, out-of-pocket expenses, lost wages, emotional anguish, and more.

Under Employment Law, please write:
Our attorneys regularly represent clients in disputes involving sex, age and race discrimination, sexual harassment, retaliatory discharge, defamation, unlawful termination, breach of employment contracts, and more.

Somewhere on the flyer, please write our slogan IN ITALICS (and probably in orange):
- You Speak. We Listen. They Pay.

In somewhat bright and bold writing, please write "CONTACT US FOR A FREE CONSULTATION TODAY!" (maybe just after our slogan?)
- And under that phrase, write:
- 731 W. Larkmoor Avenue, Suite 400 Glenfield, CA 90488
phone: 555.318.9062
fax: 555.318.9074
email: info@mkrlegal-example.com
web: www.mkrlegal-example.com

If possible, and only if there's room without it looking too busy, somewhere in the upper left corner, place our "MKR" logo.
Updates

PLEASE NOTE THAT WE CHANGED OUR GROUP PHOTO TO A SLIGHTLY EDITED ONE.  PLEASE BE SURE TO USE THE NEW ONE!!!  (We deleted the old.)

Target Market(s)

employees, lower and mid-income individuals, minority communities. However, we still want the flyer to look sleek, modern, and professional.

Industry/Entity Type

Advertising

Requirements
Must have
• Firm Name,
Photo of Partners,
Names, photos, and small description of practice areas,
Firm slogan,
"Contact us for a free consultation today!",
Firm contact info.

And only if space and overall look permits, firm "MKR" logo.

We want an overall very sleek, modern feel to our flyer. While we do want to look professional, we wanted a more approachable feel than the typical, conservative law offices.
Nice to have
• Firm "MKR" logo

Horizontal lay out, though we're open to vertical options.

```html
<!DOCTYPE html>
<html lang="en">
<head>
<meta charset="utf-8">
<title>Morvante Keldric LLP – Flyer</title>
<link href="https://fonts.googleapis.com/css2?family=Yanone+Kaffeesatz:wght@300;400;600;700&display=swap" rel="stylesheet">
<style>
  :root {
    --steel: #5b8796;
    --steel-dark: #1f3a40;
    --orange: #f26a2e;
    --silver-light: #f4f4f4;
    --silver-mid: #d6d6d6;
    --silver-dark: #c2c2c2;
    --page: #ffffff;
    --white: #ffffff;
  }
  * { margin: 0; padding: 0; box-sizing: border-box; }
  html, body {
    width: 1200px; height: 921px; overflow: hidden;
    background: var(--page);
    font-family: "Yanone Kaffeesatz", "Arial Narrow", sans-serif;
  }
  .flyer {
    position: absolute; left: 0; top: 60px;
    width: 1200px; height: 800px; overflow: hidden;
    background: radial-gradient(ellipse 620px 480px at 600px 390px, var(--silver-light) 0%, var(--silver-mid) 60%, var(--silver-dark) 100%);
  }
  .team-photo { position: absolute; left: 0; top: 0; width: 1200px; height: 800px; }
  .brand { position: absolute; left: 26px; top: 26px; }
  .brand-mark {
    width: 197px; height: 197px; background: var(--steel);
    display: flex; align-items: center; justify-content: center; gap: 14px;
  }
  .brand-mark .square { width: 34px; height: 34px; background: var(--white); }
  .brand-name { color: var(--white); font-size: 64px; font-weight: 400; letter-spacing: 4px; }
  .web { position: absolute; left: 26px; top: 222px; color: var(--steel); font-size: 34px; font-weight: 400; }
  .slogan {
    position: absolute; left: 243px; top: 16px;
    color: var(--orange); font-size: 60px; font-weight: 400; font-style: italic;
    line-height: 76px;
  }
  .practice { position: absolute; left: 24px; width: 760px; }
  .practice-head { display: flex; align-items: flex-end; gap: 7px; }
  .practice-icon { width: 83px; height: 83px; background: var(--steel-dark); flex: none; }
  .practice-title {
    color: var(--orange); font-size: 48px; font-weight: 600; line-height: 1;
    margin-bottom: -6px; letter-spacing: -0.5px;
  }
  .practice-text {
    margin-top: 12px; color: var(--steel); font-size: 27px; font-weight: 300;
    line-height: 33px; letter-spacing: -0.3px;
  }
  .injury { top: 343px; }
  .employment { top: 560px; }
  .contact {
    position: absolute; right: 24px; top: 480px; text-align: right;
    color: var(--white);
  }
  .contact-cta { color: var(--orange); font-size: 54px; font-weight: 600; line-height: 49px; letter-spacing: -0.5px; }
  .contact-address { margin-top: 8px; font-size: 26px; font-weight: 300; line-height: 33px; }
  .contact-phone { font-size: 24px; font-weight: 300; line-height: 52px; }
  .contact-phone strong { color: var(--orange); font-size: 56px; font-weight: 600; vertical-align: -4px; }
  .contact-fax { font-size: 26px; font-weight: 300; line-height: 36px; }
  .contact-email { font-size: 26px; font-weight: 300; line-height: 40px; }
  .contact-email strong { font-size: 32px; font-weight: 600; }
</style>
</head>
<body>
<main class="flyer">
  <svg class="team-photo" viewBox="0 0 1200 800" role="img" aria-label="Group photo of the three firm partners standing in an office lobby">
    <defs>
      <linearGradient id="photoTone" x1="0" y1="0" x2="1" y2="0.4">
        <stop offset="0" stop-color="#cbbfae"/>
        <stop offset="0.35" stop-color="#3a3836"/>
        <stop offset="0.55" stop-color="#ece8e3"/>
        <stop offset="0.8" stop-color="#8a6d45"/>
        <stop offset="1" stop-color="#e7e1d9"/>
      </linearGradient>
    </defs>
    <path d="M478 0 C 545 250, 770 445, 1200 486 L1200 0 Z" fill="url(#photoTone)"/>
    <path d="M478 0 C 545 250, 770 445, 1200 486" fill="none" stroke="var(--steel)" stroke-width="7"/>
  </svg>

  <div class="brand">
    <div class="brand-mark"><span class="square"></span><span class="brand-name">MKR</span></div>
  </div>
  <div class="web">www.mkrlegal-example.com</div>

  <p class="slogan">You Speak.<br>We Listen.<br>They Pay.</p>

  <section class="practice injury">
    <div class="practice-head">
      <svg class="practice-icon" viewBox="0 0 83 83" role="img" aria-label="Ambulance icon">
        <rect width="83" height="83" fill="var(--steel-dark)"/>
        <path d="M12 28 H48 V58 H12 Z M48 36 H60 L70 46 V58 H48 Z" fill="var(--white)"/>
        <rect x="35" y="22" width="8" height="6" fill="var(--white)"/>
        <path d="M27 36 h6 v6 h6 v6 h-6 v6 h-6 v-6 h-6 v-6 h6 z" fill="var(--steel-dark)"/>
        <path d="M52 39 H59 L65 45 H52 Z" fill="var(--steel-dark)"/>
        <circle cx="23" cy="59" r="6" fill="var(--white)" stroke="var(--steel-dark)" stroke-width="3"/>
        <circle cx="59" cy="59" r="6" fill="var(--white)" stroke="var(--steel-dark)" stroke-width="3"/>
      </svg>
      <h2 class="practice-title">PERSONAL INJURY:</h2>
    </div>
    <p class="practice-text">If you or a loved one are suffering from an injury or wrongful death caused by the careless or intentional acts of others, then you have the right to pursue compensation for your injury, out-of-pocket expenses, lost wages, emotional anguish, and more.</p>
  </section>

  <section class="practice employment">
    <div class="practice-head">
      <svg class="practice-icon" viewBox="0 0 83 83" role="img" aria-label="Office desk with computer icon">
        <rect width="83" height="83" fill="var(--steel-dark)"/>
        <rect x="14" y="24" width="26" height="18" fill="var(--white)"/>
        <rect x="25" y="42" width="4" height="6" fill="var(--white)"/>
        <rect x="10" y="48" width="52" height="5" fill="var(--white)"/>
        <rect x="14" y="53" width="4" height="18" fill="var(--white)"/>
        <rect x="54" y="53" width="4" height="18" fill="var(--white)"/>
        <rect x="62" y="50" width="10" height="4" fill="var(--white)"/>
        <rect x="65" y="54" width="4" height="17" fill="var(--white)"/>
      </svg>
      <h2 class="practice-title">EMPLOYMENT LAW:</h2>
    </div>
    <p class="practice-text">Our attorneys regularly represent clients in disputes involving sex, age and race discrimination, sexual harassment, retaliatory discharge, defamation, unlawful termination, breach of employment contracts, and more.</p>
  </section>

  <aside class="contact">
    <h2 class="contact-cta">Contact Us For A Free<br>Consultation Today!</h2>
    <p class="contact-address">731 W. Larkmoor Avenue,<br>Suite 400 Glenfield, CA 90488</p>
    <p class="contact-phone">phone: <strong>555.318.9062</strong></p>
    <p class="contact-fax">fax: 555.318.9074</p>
    <p class="contact-email">email: <strong>info@mkrlegal-example.com</strong></p>
  </aside>
</main>
</body>
</html>
```